Creating a Label for the Wine "Cala Brisena"

Cala Brisena
Cala Brisena means “lost mountain. Cala Brisena is a mountain far away from everything, lost in a wild place. The dimensios shoul be between 9cm x 11,5 cm and 12cm x 8 cm.

```html
<!DOCTYPE html>
<html lang="en">
<head>
<meta charset="UTF-8">
<title>Cala Brisena — Wine Label</title>
<link rel="stylesheet" href="https://fonts.googleapis.com/css2?family=Mystery+Quest&family=Josefin+Sans:wght@300;400&display=swap">
<style>
  :root {
    --paper: #e6e5da;
    --top-band: #a3120f;
    --bottom-band: #141414;
    --wine: #5c1a2e;
    --ink: #1d1b18;
    --forest: #2f7d45;
    --bark: #b8923a;
    --slate: #3f5a66;
    --river: #1f7f9a;
    --earth: #5a4420;
    --drum: #a58546;
  }
  * { margin: 0; padding: 0; box-sizing: border-box; }
  html, body {
    width: 1200px;
    height: 800px;
    overflow: hidden;
    background: var(--paper);
  }
  .label {
    position: relative;
    width: 1200px;
    height: 800px;
    background: var(--paper);
    overflow: hidden;
    font-family: "Josefin Sans", sans-serif;
    font-weight: 300;
  }
  .band { position: absolute; left: 0; width: 1200px; }
  .band--top { top: 0; height: 30px; }
  .band--bottom { bottom: 0; height: 34px; }

  .landscape {
    position: absolute;
    left: 0; top: 0;
    width: 1200px; height: 320px;
  }

  .wine-name {
    position: absolute;
    left: 0; top: 338px;
    width: 1200px;
    text-align: center;
    font-family: "Mystery Quest", serif;
    font-weight: 400;
    font-size: 145px;
    line-height: 1;
    color: var(--wine);
    letter-spacing: 10px;
  }

  .appellation {
    position: absolute;
    left: 778px; top: 484px;
    width: 300px;
    text-align: center;
    font-size: 26px;
    line-height: 36px;
    letter-spacing: 2px;
    color: var(--ink);
  }

  .details {
    position: absolute;
    left: 136px; top: 534px;
    width: 280px;
    text-align: center;
    color: var(--ink);
  }
  .details__region {
    font-size: 29px;
    line-height: 32px;
    letter-spacing: 2.5px;
    color: var(--wine);
    margin-bottom: 12px;
  }
  .details__fact {
    font-size: 24px;
    line-height: 33px;
    letter-spacing: 1.5px;
  }
  .details__flourish {
    display: block;
    margin: 12px auto 8px;
  }
  .details__origin {
    font-size: 24px;
    letter-spacing: 2.5px;
  }

  .figure-art {
    position: absolute;
    left: 500px; top: 482px;
    width: 295px; height: 272px;
  }

  .abv {
    position: absolute;
    left: 940px; top: 735px;
    font-size: 21px;
    letter-spacing: 1.5px;
    color: var(--ink);
  }
</style>
</head>
<body>
<main class="label">
  <svg class="band band--top" viewBox="0 0 1200 30" aria-hidden="true">
    <path d="M0 0H1200V16C1150 22 1100 12 1050 18 1000 24 950 14 900 20 850 14 800 22 750 17 700 12 650 21 600 16 550 22 500 13 450 19 400 23 350 15 300 20 250 14 200 22 150 16 100 21 50 14 0 19Z" fill="var(--top-band)"/>
  </svg>

  <svg class="landscape" viewBox="0 0 1200 320" role="img" aria-label="Illustration of a wild landscape: a row of trees, a hut and animals framing mirrored snowy mountains, rivers and an eye motif">
    <defs>
      <linearGradient id="landscapeTone" x1="0" y1="0" x2="0" y2="1">
        <stop offset="0" stop-color="var(--forest)"/>
        <stop offset="0.45" stop-color="var(--bark)"/>
        <stop offset="0.7" stop-color="var(--slate)"/>
        <stop offset="1" stop-color="var(--river)"/>
      </linearGradient>
    </defs>
    <path d="M20 85Q20 60 45 60H1150Q1172 60 1172 85V180Q1172 205 1148 205H962Q948 250 880 270H652Q622 300 600 300Q578 300 548 270H320Q252 250 238 205H45Q20 205 20 180Z" fill="url(#landscapeTone)" opacity="0.42"/>
  </svg>

  <h1 class="wine-name">CALA BRISENA</h1>

  <p class="appellation">Appellation<br>Control Statement</p>

  <section class="details">
    <p class="details__region">VIN DE<br>BOURGOGNE</p>
    <p class="details__fact">SINCE 1964</p>
    <p class="details__fact">750 ML</p>
    <svg class="details__flourish" width="54" height="18" viewBox="0 0 54 18" role="img" aria-label="Small decorative flourish">
      <rect x="0" y="6" width="54" height="6" rx="3" fill="var(--ink)" opacity="0.45"/>
    </svg>
    <p class="details__origin">Product of Italy</p>
  </section>

  <svg class="figure-art" viewBox="0 0 295 272" role="img" aria-label="Illustration of a dancing figure with raised arms beside a hand drum">
    <defs>
      <linearGradient id="figureTone" x1="0" y1="0" x2="1" y2="1">
        <stop offset="0" stop-color="var(--earth)"/>
        <stop offset="1" stop-color="var(--drum)"/>
      </linearGradient>
    </defs>
    <rect x="0" y="0" width="295" height="272" rx="60" fill="url(#figureTone)" opacity="0.3"/>
  </svg>

  <p class="abv">ALC. 14.5%</p>

  <svg class="band band--bottom" viewBox="0 0 1200 34" aria-hidden="true">
    <path d="M0 34H1200V12C1150 6 1100 16 1050 10 1000 4 950 14 900 8 850 14 800 6 750 12 700 16 650 8 600 13 550 6 500 15 450 9 400 5 350 13 300 8 250 14 200 6 150 12 100 7 50 14 0 9Z" fill="var(--bottom-band)"/>
  </svg>
</main>
</body>
</html>
```